Biz card, stationary for geriatric clinic
ValdoNorte Residence & Geriatric SPA
Biz card, stationary for geriatric clinic - Health
Creative Brief
Professional
Dra. Tereza Lopes Amaral
Diretora
Vale Alto - RS
tereza@valdonorte.example
www.valdonorte.example
We will need stationary i.e. letterhead, envelope, etc. For all business cards we need editable files to change for multiple employees.
Mailing address: Rua Oitenta e sete, 418. CEP 41270-000 | Bairro Jardim Vale Alto - RS

```html
<!DOCTYPE html>
<html lang="pt">
<head>
<meta charset="utf-8">
<title>ValdoNorte – Business Card</title>
<link rel="stylesheet" href="https://fonts.googleapis.com/css2?family=Crimson+Text:ital,wght@0,400;0,700;1,400&display=swap">
<style>
  :root {
    --page: #ece8df;
    --olive: #a39c5f;
    --olive-light: #b5ae72;
    --olive-dark: #8a834b;
    --band: #ffffff;
    --ink-gold: #8f7a2a;
    --ink-soft: #6e6632;
    --on-olive: #fbf8ea;
  }
  * { box-sizing: border-box; margin: 0; padding: 0; }
  html, body { width: 1200px; height: 901px; overflow: hidden; }
  body {
    background: var(--page);
    font-family: "Crimson Text", Georgia, serif;
    display: flex; flex-direction: column; align-items: center; justify-content: center;
    gap: 56px;
  }
  .card {
    position: relative; width: 620px; height: 354px; overflow: hidden;
    box-shadow: 0 6px 18px rgba(60,50,20,.18);
  }
  .card__pattern {
    position: absolute; inset: 0;
    background: radial-gradient(ellipse at 50% 40%, var(--olive-light), var(--olive) 60%, var(--olive-dark));
  }
  .brand { display: flex; align-items: center; gap: 14px; color: var(--on-olive); }
  .brand__mark { width: 58px; height: 58px; border-radius: 50%; background: var(--on-olive); opacity: .9; }
  .brand__name { font-size: 42px; font-weight: 400; line-height: 1; }

  /* back side */
  .card--back .card__body {
    position: absolute; inset: 0; display: flex; flex-direction: column;
    align-items: center; justify-content: center; color: var(--on-olive);
  }
  .card--back .brand { flex-direction: column; gap: 10px; }
  .card--back .brand__mark { width: 70px; height: 70px; }
  .card--back .brand__name { font-size: 50px; }
  .mailing { margin-top: 14px; font-size: 13px; line-height: 1.3; text-align: center; }

  /* front side */
  .band { position: absolute; inset: 0; width: 100%; height: 100%; }
  .card--front .brand { position: absolute; left: 34px; top: 26px; }
  .site { position: absolute; left: 108px; top: 86px; color: var(--on-olive); font-size: 15px; }
  .person { position: absolute; left: 0; right: 0; top: 166px; text-align: center; }
  .person__name { color: var(--ink-gold); font-size: 25px; font-weight: 700; }
  .person__role { color: var(--ink-soft); font-size: 19px; font-style: italic; }
  .contact {
    position: absolute; color: var(--on-olive); font-size: 15px; line-height: 1.35;
  }
  .contact--left { left: 34px; bottom: 26px; }
  .contact--right { right: 34px; bottom: 58px; }
  .contact dt { display: inline; }
  .contact dd { display: inline; margin-left: 6px; }
</style>
</head>
<body>

  <article class="card card--back" aria-label="Business card, back">
    <div class="card__pattern" role="img" aria-label="Olive damask pattern background"></div>
    <div class="card__body">
      <div class="brand">
        <span class="brand__mark"></span>
        <span class="brand__name">ValdoNorte</span>
      </div>
      <p class="mailing">
        Rua Oitenta e sete, 418.<br>
        CEP 41270-000 | Bairro Jardim<br>
        Vale Alto - RS
      </p>
    </div>
  </article>

  <article class="card card--front" aria-label="Business card, front">
    <div class="card__pattern" role="img" aria-label="Olive damask pattern background"></div>
    <svg class="band" viewBox="0 0 620 354" preserveAspectRatio="none" aria-hidden="true">
      <path d="M0 140 C180 128 420 108 620 92 L620 204 C420 220 200 246 0 272 Z" fill="var(--band)"/>
    </svg>
    <div class="brand">
      <span class="brand__mark"></span>
      <span class="brand__name">ValdoNorte</span>
    </div>
    <p class="site">www.valdonorte.example</p>
    <div class="person">
      <p class="person__name">Dra. Tereza Lopes Amaral</p>
      <p class="person__role">Diretora</p>
    </div>
    <dl class="contact contact--left">
      <div><dt>address:</dt><dd>Vale Alto - RS</dd></div>
      <div><dt>email:</dt><dd>tereza@valdonorte.example</dd></div>
    </dl>
    <dl class="contact contact--right">
      <div><dt>phone:</dt><dd>(051) 3000-4127</dd></div>
      <div><dt>fax:</dt><dd>(051) 9000-5318</dd></div>
    </dl>
  </article>

</body>
</html>
```